Business Card/ Car Magnet/ Polo Shirt/ Envelope/ Letterhead Design Project
Birchmont Property Valuations, LLC.
Business Card/ Car Magnet/ Polo Shirt/ Envelope/ Letterhead Design Project - Real Estate
Creative Brief
Professional
Gus Talbottine
State Certified Residential Real Estate Appraiser
14 Coldmeadow Ln Sewell, NJ 08080
gtalbottine@birchmontvaluations.example
valuemarkhq.example
NJ- 57RC00913400 PA- RL284615 DE- X2-0000317
Please be creative...
gust1983 gust1983
Hello, Just wanted to clarify some of the common questions asked so far. The colors to incorporate would be blue, green and white (unless of course you would like to incorporate other colors for creativity) . please feel free to incorporate them any way you see fit. The polo shirts will be done on white, black and royal blue shirts. Please be as creative as you like. Thanks you for your efforts and for participating! Please reply back with any further questions. Thanks! BPV

```html
<!DOCTYPE html>
<html lang="en">
<head>
<meta charset="utf-8">
<title>Birchmont Property Valuations – Business Cards</title>
<link rel="stylesheet" href="https://fonts.googleapis.com/css2?family=Cinzel:wght@600&family=Michroma&display=swap">
<style>
  :root{
    --page:#e9ebee;
    --card:#ffffff;
    --brand-blue:#1f63b5;
    --brand-navy:#1b3f8c;
    --brand-green:#5aa832;
    --band-deep:#0c5fc0;
    --band-light:#2fa3ee;
    --ink-on-band:#ffffff;
  }
  *{margin:0;padding:0;box-sizing:border-box}
  html,body{width:1200px;height:899px;overflow:hidden;background:var(--page)}
  .canvas{position:relative;width:1200px;height:899px}
  .card{position:absolute;width:600px;height:343px;background:var(--card);
        box-shadow:0 10px 28px rgba(0,0,0,.18);overflow:hidden}
  .card--brand{left:520px;top:70px}
  .card--contact{left:120px;top:470px}

  .brand{position:absolute;text-align:center;font-family:"Cinzel",serif;font-weight:600;color:var(--brand-blue)}
  .brand__row{display:flex;align-items:center;justify-content:center;gap:10px}
  .brand__mark{width:22px;height:22px;border-radius:50%;background:var(--brand-green)}
  .brand__name{font-size:58px;line-height:1;letter-spacing:2px}
  .brand__tagline{font-size:11px;letter-spacing:.5px;margin-top:6px;color:var(--brand-blue)}
  .card--brand .brand{left:0;right:0;top:112px}
  .card--contact .brand{left:28px;top:28px}
  .card--contact .brand__name{font-size:44px}
  .card--contact .brand__mark{width:18px;height:18px}
  .card--contact .brand__tagline{font-size:9px}

  .band{position:absolute;left:0;top:0;width:600px;height:343px}

  .contacts{position:absolute;left:34px;top:198px;list-style:none;
            font-family:"Michroma",sans-serif;font-size:9px;color:var(--ink-on-band)}
  .contacts li{display:flex;align-items:center;gap:8px;height:17px}
  .contacts svg{width:10px;height:10px;fill:var(--ink-on-band)}
  .website{position:absolute;left:34px;bottom:26px;font-family:"Michroma",sans-serif;
           font-size:11px;color:var(--ink-on-band)}
  .person{position:absolute;right:40px;top:112px;text-align:right;font-family:"Michroma",sans-serif}
  .person__name{font-size:17px;letter-spacing:1px;color:var(--brand-navy)}
  .person__role{font-size:12px;color:var(--brand-navy);margin-top:6px}
  .address{position:absolute;right:40px;top:258px;width:210px;font-family:"Michroma",sans-serif;
           font-size:9px;line-height:1.6;color:var(--ink-on-band)}
</style>
</head>
<body>
<main class="canvas">
  <section class="card card--brand" aria-label="Business card front">
    <div class="brand">
      <div class="brand__row"><span class="brand__mark"></span><span class="brand__name">BPV</span></div>
      <div class="brand__tagline">BIRCHMONT PROPERTY VALUATIONS, LLC.</div>
    </div>
  </section>

  <section class="card card--contact" aria-label="Business card back">
    <svg class="band" viewBox="0 0 600 343" aria-hidden="true">
      <defs>
        <linearGradient id="bandFill" x1="0" y1="0" x2="1" y2="0.4">
          <stop offset="0" stop-color="var(--band-deep)"/>
          <stop offset="1" stop-color="var(--band-light)"/>
        </linearGradient>
      </defs>
      <path d="M0 170 C150 175 300 200 600 245 L600 343 L0 343 Z" fill="url(#bandFill)"/>
      <path d="M0 160 C160 164 320 188 600 236" fill="none" stroke="var(--brand-green)" stroke-width="5"/>
    </svg>

    <div class="brand">
      <div class="brand__row"><span class="brand__mark"></span><span class="brand__name">BPV</span></div>
      <div class="brand__tagline">BIRCHMONT PROPERTY VALUATIONS, LLC.</div>
    </div>

    <ul class="contacts">
      <li><svg viewBox="0 0 10 10"><path d="M2 0h2l1 3-1.5 1a6 6 0 0 0 2.5 2.5L7 5l3 1v2c0 1-1 2-2 2A8 8 0 0 1 0 2C0 1 1 0 2 0z"/></svg>012 555 0147</li>
      <li><svg viewBox="0 0 10 10"><rect x="3" y="0" width="4" height="10" rx="1"/></svg>012 555 0147</li>
      <li><svg viewBox="0 0 10 10"><rect x="0" y="3" width="10" height="6" rx="1"/><rect x="2" y="0" width="6" height="3"/></svg>012 555 0148</li>
      <li><svg viewBox="0 0 10 10"><path d="M0 2h10v6H0zM0 2l5 3 5-3"/></svg>gtalbottine@birchmontvaluations.example</li>
    </ul>

    <div class="website">valuemarkhq.example</div>

    <div class="person">
      <div class="person__name">GUS TALBOTTINE</div>
      <div class="person__role">Managing Director</div>
    </div>

    <div class="address">14 Coldmeadow Ln<br>Sewell, NJ 08080</div>
  </section>
</main>
</body>
</html>
```